Dune crest Website

We need a simple web page design for our businessWe procure and dispose of earthmoving construction equipmentwe also find construction equipment for our customers using our global contacts

Number of Pages Required

1 page

```html
<!DOCTYPE html>
<html lang="en">
<head>
<meta charset="utf-8">
<title>Dune crest — Earthmoving Equipment</title>
<link href="https://fonts.googleapis.com/css2?family=Poppins:wght@400;500;600;700&display=swap" rel="stylesheet">
<style>
:root{
  --blue:#12a5ec;
  --blue-dark:#0f8fd0;
  --ink:#333333;
  --muted:#6f6f6f;
  --white:#ffffff;
  --light:#f2f2f2;
  --footer:#111111;
  --field:#f4f4f4;
  --line:#dddddd;
}
*{box-sizing:border-box;margin:0;padding:0}
html,body{width:1200px;height:3163px;overflow:hidden}
body{font-family:"Poppins",sans-serif;color:var(--ink);background:var(--white);position:relative}
a{text-decoration:none;color:inherit}

.site-header{position:absolute;left:0;top:0;width:1200px;height:86px;background:var(--white);display:flex;align-items:center;justify-content:space-between;padding:0 116px}
.brand{display:flex;align-items:center;gap:14px;font-weight:600;font-size:24px;color:var(--blue)}
.brand-dot{width:46px;height:46px;border-radius:50%;background:var(--blue)}
.main-nav{display:flex;gap:36px;font-size:16px;color:#444}
.main-nav .active{color:var(--blue)}

.hero{position:absolute;left:0;top:86px;width:1200px;height:600px;background:linear-gradient(180deg,#4a4a52 0%,#8a5a3a 35%,#c77a2e 55%,#5a3520 80%,#1c130e 100%)}
.hero-title{position:absolute;left:114px;top:176px;font-size:49px;font-weight:600;color:var(--white)}
.hero-text{position:absolute;left:114px;top:242px;width:500px;font-size:21px;line-height:31px;font-weight:500;color:var(--white)}
.btn{display:inline-flex;align-items:center;justify-content:center;background:var(--blue);color:var(--white);font-weight:600;border-radius:30px}
.hero .btn{position:absolute;left:114px;top:353px;width:182px;height:57px;font-size:18px}
.hero-dots{position:absolute;left:1132px;top:272px;display:flex;flex-direction:column;gap:10px;align-items:center}
.hero-dots span{width:10px;height:10px;border-radius:50%;background:var(--white)}
.hero-dots .on{width:18px;height:18px;background:transparent;border:3px solid var(--white);position:relative}
.hero-dots .on::after{content:"";position:absolute;left:3px;top:3px;width:6px;height:6px;border-radius:50%;background:var(--white)}

.services{position:absolute;left:0;top:686px;width:1200px;height:506px;background:var(--white)}
.services-backdrop{position:absolute;right:0;top:250px;width:500px;height:256px;background:radial-gradient(ellipse at 70% 70%,rgba(230,190,120,.35),rgba(255,255,255,0) 70%)}
.service-card{position:absolute;top:59px;width:310px;text-align:center}
.service-card .photo{width:310px;height:190px}
.service-card h3{margin-top:22px;font-size:20px;font-weight:600;color:var(--blue)}
.service-card p{margin:8px auto 0;width:290px;font-size:14px;line-height:23px;color:var(--muted)}
.service-card .more{display:inline-block;margin-top:12px;font-size:16px;font-weight:500;color:var(--blue);border-bottom:2px solid var(--blue);line-height:20px}

.quote{position:absolute;left:0;top:1192px;width:1200px;height:428px;background:linear-gradient(90deg,#2c2f33 0%,#3c3e40 50%,#4a4536 75%,#2a2a2a 100%)}
.quote-eyebrow{position:absolute;left:0;top:48px;width:1200px;text-align:center;font-size:20px;font-weight:500;color:var(--white)}
.quote-title{position:absolute;left:0;top:72px;width:1200px;text-align:center;font-size:39px;font-weight:600;color:var(--white)}
.quote-form{position:absolute;left:278px;top:137px;width:642px;height:236px;background:var(--white)}
.field-label{position:absolute;font-size:15px;color:#555}
.field{position:absolute;height:46px;background:var(--field);border:1px solid var(--line);font-size:11px;color:#999;padding:0 16px;display:flex;align-items:center}
.quote-form .btn{position:absolute;left:332px;top:145px;width:196px;height:46px;border-radius:0;font-size:15px}

.projects{position:absolute;left:0;top:1620px;width:1200px;height:757px}
.section-title{position:absolute;left:0;width:1200px;text-align:center;font-size:39px;font-weight:600;color:var(--blue)}
.project{position:absolute;width:379px;height:249px}
.project span{position:absolute;left:34px;bottom:18px;font-size:22px;font-weight:600;color:var(--white)}

.testimonials{position:absolute;left:0;top:2377px;width:1200px;height:443px;background:var(--light)}
.testimonial{position:absolute;top:137px;width:455px;height:148px;background:var(--white);padding:22px 30px 0 36px;font-size:15px;line-height:24px;color:var(--muted)}
.testimonial::before{content:"";position:absolute;left:0;top:28px;width:4px;height:58px;background:var(--blue)}
.testimonial .read{display:block;margin-top:4px;font-size:16px;font-weight:500;color:var(--blue)}
.author{position:absolute;top:306px;display:flex;align-items:center;gap:12px}
.author .avatar{width:60px;height:60px;border-radius:50%;background:linear-gradient(135deg,#c9b39a,#7d6650)}
.author strong{display:block;font-size:17px;font-weight:500;color:var(--blue)}
.author small{display:block;font-size:12px;font-weight:600;color:#222}

.site-footer{position:absolute;left:0;top:2820px;width:1200px;height:343px;background:var(--footer);color:var(--white)}
.footer-col{position:absolute;top:52px}
.footer-col h4{font-size:18px;font-weight:600;margin-bottom:26px}
.footer-col p,.footer-col li{font-size:14px;line-height:26px}
.footer-col ul{list-style:none}
.social{display:flex;gap:14px;margin-top:20px}
.social span{width:28px;height:28px;border-radius:50%;background:var(--white)}
.contact-line{font-size:13px;line-height:21px;margin-bottom:18px}
.contact-line b{font-weight:500}
.copyright{position:absolute;left:0;top:298px;width:1200px;text-align:center;font-size:14px}
</style>
</head>
<body>

<header class="site-header">
  <a class="brand" href="#"><span class="brand-dot"></span>Dune crest</a>
  <nav class="main-nav">
    <a class="active" href="#">Home</a><a href="#">About Us</a><a href="#">Services</a><a href="#">Projects</a><a href="#">Blog</a><a href="#">Contact Us</a>
  </nav>
</header>

<section class="hero" role="img" aria-label="Wheel loader silhouetted against a sunset sky">
  <h1 class="hero-title">Welcome To Dune crest</h1>
  <p class="hero-text">Lorem ipsum dolor sit amet, consectetur adipiscing elit, sed do eiusmod tempor incididunt ut labore et dolore magna aliqua.</p>
  <a class="btn" href="#">Learn More</a>
  <div class="hero-dots"><span class="on"></span><span></span><span></span></div>
</section>

<section class="services">
  <div class="services-backdrop" role="img" aria-label="Faint wheel loader in the background"></div>
  <article class="service-card" style="left:112px">
    <div class="photo" role="img" aria-label="Bulldozer at sunset" style="background:linear-gradient(180deg,#d9a47a,#a87248 60%,#6b4a33)"></div>
    <h3>Sed ut perspiciatis unde</h3>
    <p>Lorem ipsum dolor sit amet, consectetur adipiscing elit, sed do eiusmod tempor incididunt ut labore et dolore magna aliqua.</p>
    <a class="more" href="#">Learn More</a>
  </article>
  <article class="service-card" style="left:445px">
    <div class="photo" role="img" aria-label="Yellow wheel loader under blue sky" style="background:linear-gradient(180deg,#3f78b8,#c9a23a 60%,#6c5a3a)"></div>
    <h3>Sed ut perspiciatis unde</h3>
    <p>Lorem ipsum dolor sit amet, consectetur adipiscing elit, sed do eiusmod tempor incididunt ut labore et dolore magna aliqua.</p>
    <a class="more" href="#">Learn More</a>
  </article>
  <article class="service-card" style="left:776px">
    <div class="photo" role="img" aria-label="Backhoe loader at dusk" style="background:linear-gradient(180deg,#3a5470,#c9913e 55%,#3a2f24)"></div>
    <h3>Sed ut perspiciatis unde</h3>
    <p>Lorem ipsum dolor sit amet, consectetur adipiscing elit, sed do eiusmod tempor incididunt ut labore et dolore magna aliqua.</p>
    <a class="more" href="#">Learn More</a>
  </article>
</section>

<section class="quote" role="img" aria-label="Dark photo of a wheel loader behind the quote form">
  <p class="quote-eyebrow">Contact Today</p>
  <h2 class="quote-title">Free Quote</h2>
  <form class="quote-form">
    <label class="field-label" style="left:40px;top:30px">Your Name</label>
    <div class="field" style="left:40px;top:61px;width:275px">Your Name</div>
    <label class="field-label" style="left:332px;top:30px">Your Number</label>
    <div class="field" style="left:332px;top:61px;width:272px">Phone Number</div>
    <label class="field-label" style="left:40px;top:116px">How We Can Help?</label>
    <div class="field" style="left:40px;top:145px;width:275px">Request A Consultation?</div>
    <a class="btn" href="#">SEND MESSAGE</a>
  </form>
</section>

<section class="projects">
  <h2 class="section-title" style="top:52px">Recent Projects</h2>
  <div class="project" style="left:15px;top:147px;background:linear-gradient(180deg,#2c3a4c,#4a4c44 60%,#2a2a26)" role="img" aria-label="Excavator under a stormy sky"><span>Lorem ipsum dolor</span></div>
  <div class="project" style="left:411px;top:147px;background:linear-gradient(180deg,#1c2c54,#3b4a6a 50%,#6a6a66)" role="img" aria-label="Loader at a lit site at night"><span>Lorem ipsum dolor</span></div>
  <div class="project" style="left:806px;top:147px;background:linear-gradient(160deg,#f3d27a,#c97a3a 40%,#4a5a6a)" role="img" aria-label="Worker in a hard hat at sunrise"><span>Lorem ipsum dolor</span></div>
  <div class="project" style="left:15px;top:415px;background:linear-gradient(180deg,#3a7ac0,#d9b23a 55%,#7a6a4a)" role="img" aria-label="Yellow excavators under blue sky"><span>Lorem ipsum dolor</span></div>
  <div class="project" style="left:411px;top:415px;background:linear-gradient(180deg,#d9a060,#a07040 45%,#4a3a2a)" role="img" aria-label="Wheel loader bucket in a quarry"><span>Lorem ipsum dolor</span></div>
  <div class="project" style="left:806px;top:415px;background:linear-gradient(180deg,#3a4e6a,#5a6678 55%,#2c2c30)" role="img" aria-label="Excavator arm against a cloudy sky"><span>Lorem ipsum dolor</span></div>
</section>

<section class="testimonials">
  <h2 class="section-title" style="top:48px">Testimonials</h2>
  <blockquote class="testimonial" style="left:129px">Lorem ipsum dolor sit amet, consectetur adipiscing elit, sed do eiusmod tempor incididunt ut labore et dolore magna aliqua.<a class="read" href="#">Read More</a></blockquote>
  <blockquote class="testimonial" style="left:610px">Lorem ipsum dolor sit amet, consectetur adipiscing elit, sed do eiusmod tempor incididunt ut labore et dolore magna aliqua.<a class="read" href="#">Read More</a></blockquote>
  <div class="author" style="left:131px"><div class="avatar" role="img" aria-label="Client portrait"></div><div><strong>Alan Reyes</strong><small>USA</small></div></div>
  <div class="author" style="left:613px"><div class="avatar" role="img" aria-label="Client portrait"></div><div><strong>Maya Holt</strong><small>UK</small></div></div>
</section>

<footer class="site-footer">
  <div class="footer-col" style="left:116px;width:240px">
    <h4>About Us</h4>
    <p>Lorem ipsum dolor sit amet, consectetur adipiscing elit, sed do eiusmod tempor</p>
    <div class="social"><span></span><span></span><span></span><span></span></div>
  </div>
  <div class="footer-col" style="left:434px">
    <h4>Quick Links</h4>
    <ul><li>Home</li><li>About Us</li><li>Services</li><li>Projects</li><li>Blog</li></ul>
  </div>
  <div class="footer-col" style="left:647px">
    <h4>Support</h4>
    <ul><li>Contact Us</li><li>Privacy Policy</li><li>Terms &amp; Conditions</li></ul>
  </div>
  <div class="footer-col" style="left:880px;width:240px">
    <h4>Contact Us</h4>
    <p class="contact-line"><b>Address:</b> #14, 88 Ridge Road<br>410 Quarry Bend Ave, 300,<br>#215 Millbrook, GA 30455</p>
    <p class="contact-line"><b>Phone:</b> (0471) 552 018</p>
    <p class="contact-line"><b>Email:</b> hello@dunecrest.com.au</p>
  </div>
  <p class="copyright">© 2018 Copyrights | All Rights Reserved</p>
</footer>

</body>
</html>
```